World Class Presentation folder for a National Designer of innovative building products

We are a National Designer, Manufacturer, and distributor of aluminum and stainless Balconies, Railings, Sunshades, and Patio Covers. We sell our products and services to the very best commercial condo and residential builders in the country. This Brochure folder will be the first piece of literature that we give to our customers, and want to WOW them at first glance with a world-class design and look.

We already have a logo and website but would like you to visit https://velmorafabworks.example and view the projects and product information to help inspire you to create an award-winning piece of literature for us.

Besides putting literature in it, the folder must have a place to hold a business card.

Thank you in advance for your great designs, and I look forward to working with you.
Dolan Fratheringe
President | Pacific, WA
418.627.5190 ext 305

```html
<!DOCTYPE html>
<html lang="en">
<head>
<meta charset="utf-8">
<title>Velmora Fabworks Presentation Folder</title>
<link href="https://fonts.googleapis.com/css2?family=Montserrat:wght@400;500;600;700&family=Source+Sans+3:wght@400;600&display=swap" rel="stylesheet">
<style>
  :root {
    --red: #c8203f;
    --charcoal: #1f1f1f;
    --charcoal-2: #2e2e2e;
    --ink: #2a2a2a;
    --white: #ffffff;
    --page: #d9d9d9;
    --muted: #3a3a3a;
  }
  * { margin: 0; padding: 0; box-sizing: border-box; }
  html, body { width: 1200px; height: 1043px; overflow: hidden; background: var(--page); }
  .stage { position: relative; width: 1200px; height: 1043px; }
  .folder {
    position: absolute; left: 125px; top: 32px;
    width: 864px; height: 890px;
    transform: scale(1.1); transform-origin: 0 0;
    font-family: "Source Sans 3", sans-serif;
  }
  .folder-art { position: absolute; inset: 0; width: 864px; height: 890px; }
  .abs { position: absolute; }

  .brand-top {
    left: 457px; top: 28px; width: 200px;
    font-family: "Montserrat", sans-serif; font-weight: 700;
    font-size: 24px; line-height: 1.05; letter-spacing: 1px;
    color: var(--ink); text-transform: uppercase;
    display: flex; align-items: center; gap: 10px;
  }
  .brand-top .mark { width: 14px; height: 14px; background: var(--red); flex: none; }

  .brand-panel {
    left: 30px; top: 172px;
    font-family: "Montserrat", sans-serif; font-weight: 700;
    font-size: 19px; line-height: 1.1; letter-spacing: 1px;
    color: var(--white); text-transform: uppercase;
  }
  .tagline {
    left: 30px; top: 246px; width: 250px;
    font-family: "Montserrat", sans-serif; font-weight: 500;
    font-size: 11.2px; line-height: 1.1; color: var(--white);
  }
  .products-title {
    left: 29px; top: 300px;
    font-family: "Montserrat", sans-serif; font-weight: 400;
    font-size: 19px; color: var(--red); letter-spacing: 0.3px;
  }
  .product-list { left: 28px; top: 332px; list-style: none; }
  .product-list li {
    display: flex; align-items: center; gap: 5px;
    font-size: 11px; line-height: 17.4px; color: var(--white);
  }
  .product-list svg { width: 10px; height: 10px; flex: none; }

  .contact { top: 591px; font-size: 10px; line-height: 13.6px; color: var(--muted); }
  .contact h3 {
    font-family: "Montserrat", sans-serif; font-weight: 600;
    font-size: 11px; color: var(--red); margin-bottom: 4px; letter-spacing: 0.2px;
  }
  .contact p { display: flex; align-items: flex-start; gap: 6px; }
  .contact svg { width: 9px; height: 10px; flex: none; margin-top: 2px; }
  .contact .indent { padding-left: 15px; }
  .contact-wa { left: 34px; }
  .contact-or { left: 278px; }

  .headline {
    left: 448px; top: 585px; width: 160px;
    font-family: "Montserrat", sans-serif; font-weight: 600;
    font-size: 13.2px; line-height: 17px; color: var(--ink); text-transform: uppercase;
  }
  .web {
    left: 450px; top: 651px;
    display: flex; align-items: center; gap: 6px;
    font-family: "Montserrat", sans-serif; font-weight: 500;
    font-size: 11px; color: var(--white);
  }
  .web svg { width: 11px; height: 11px; }
</style>
</head>
<body>
<div class="stage">
  <div class="folder">
    <svg class="folder-art" viewBox="0 0 864 890" xmlns="http://www.w3.org/2000/svg">
      <defs>
        <linearGradient id="panel" x1="0" y1="0" x2="1" y2="0">
          <stop offset="0" stop-color="#1c1c1c"/>
          <stop offset="1" stop-color="#333333"/>
        </linearGradient>
        <linearGradient id="photo" x1="0" y1="0" x2="0" y2="1">
          <stop offset="0" stop-color="#8fb7de"/>
          <stop offset="0.35" stop-color="#8a9a6a"/>
          <stop offset="0.6" stop-color="#4a4a44"/>
          <stop offset="1" stop-color="#3a302b"/>
        </linearGradient>
        <linearGradient id="hexA" x1="0" y1="0" x2="0" y2="1">
          <stop offset="0" stop-color="#a7c3df"/>
          <stop offset="1" stop-color="#3c3c3c"/>
        </linearGradient>
        <linearGradient id="hexB" x1="0" y1="0" x2="0" y2="1">
          <stop offset="0" stop-color="#b6cce0"/>
          <stop offset="0.6" stop-color="#a66b52"/>
          <stop offset="1" stop-color="#6d9a4a"/>
        </linearGradient>
        <linearGradient id="hexC" x1="0" y1="0" x2="0" y2="1">
          <stop offset="0" stop-color="#e9e9e6"/>
          <stop offset="0.6" stop-color="#7a6a5a"/>
          <stop offset="1" stop-color="#7fa85a"/>
        </linearGradient>
        <linearGradient id="pocket" x1="0" y1="0" x2="1" y2="1">
          <stop offset="0" stop-color="#383838"/>
          <stop offset="0.7" stop-color="#2a2a2a"/>
          <stop offset="1" stop-color="#111111"/>
        </linearGradient>
      </defs>

      <!-- cover -->
      <rect class="cover" x="0" y="0" width="864" height="683" fill="var(--white)"/>
      <rect class="dark-band" x="0" y="108" width="864" height="460" fill="url(#panel)"/>
      <path class="photo-hero" role="img" aria-label="Photo of a rooftop terrace with wicker lounge chairs, wood decking and city towers behind"
            d="M452 127 L864 127 L864 550 L150 550 Z" fill="url(#photo)"/>
      <path class="accent-swoosh" d="M422 127 Q438 123 452 127 L150 550 L126 550 Q300 300 422 127 Z" fill="var(--red)"/>

      <!-- project hexagons -->
      <polygon role="img" aria-label="Photo of glass balcony railing on a tower" points="712,415 761,443.5 761,500.5 712,529 663,500.5 663,443.5" fill="url(#hexA)" stroke="#fff" stroke-width="3"/>
      <polygon role="img" aria-label="Photo of apartment building with balconies" points="659,508 708,536.5 708,593.5 659,622 610,593.5 610,536.5" fill="url(#hexB)" stroke="#fff" stroke-width="3"/>
      <polygon role="img" aria-label="Photo of white patio cover over a porch" points="786,498 855,538 855,618 786,658 717,618 717,538" fill="url(#hexC)" stroke="#fff" stroke-width="3"/>

      <!-- value icons -->
      <g class="value-icons" fill="none" stroke="var(--red)" stroke-width="2">
        <circle cx="40" cy="469" r="13.5"/>
        <circle cx="82" cy="469" r="13.5"/>
        <circle cx="127" cy="469" r="13.5"/>
      </g>
      <g fill="var(--red)">
        <rect x="32" y="465" width="16" height="7" rx="3"/>
        <rect x="78" y="462" width="8" height="14" rx="1"/>
        <rect x="119" y="464" width="16" height="10" rx="2"/>
      </g>

      <!-- contact divider and web bar -->
      <line x1="217" y1="592" x2="217" y2="662" stroke="#cfcfcf" stroke-width="1"/>
      <path class="web-bar" d="M435 648 L643 648 L650 670 L435 670 Z" fill="var(--red)"/>

      <!-- pocket with card slits -->
      <path class="pocket" d="M434 687 L864 687 L864 890 L454 890 Z" fill="url(#pocket)"/>
      <line x1="560" y1="753" x2="585" y2="729" stroke="#8a8a8a" stroke-width="1"/>
      <line x1="733" y1="847" x2="760" y2="822" stroke="#8a8a8a" stroke-width="1"/>
    </svg>

    <div class="abs brand-top"><span class="mark"></span><span>Velmora<br>Fabworks</span></div>

    <div class="abs brand-panel">Velmora<br>Fabworks</div>
    <p class="abs tagline">PREMIER MANUFACTURER &amp; DISTRIBUTER OF ALUMINUM RAILING, BALCONY, AND SUNSHADE SYSTEMS</p>
    <h2 class="abs products-title">OUR PRODUCTS</h2>
    <ul class="abs product-list">
      <li><svg viewBox="0 0 10 10"><circle cx="5" cy="5" r="4.2" fill="none" stroke="var(--red)" stroke-width="1.2"/><path d="M3 5.2 L4.5 6.5 L7 3.8" fill="none" stroke="var(--red)" stroke-width="1.2"/></svg>Railling System</li>
      <li><svg viewBox="0 0 10 10"><circle cx="5" cy="5" r="4.2" fill="none" stroke="var(--red)" stroke-width="1.2"/><path d="M3 5.2 L4.5 6.5 L7 3.8" fill="none" stroke="var(--red)" stroke-width="1.2"/></svg>Stainless Steel Cable</li>
      <li><svg viewBox="0 0 10 10"><circle cx="5" cy="5" r="4.2" fill="none" stroke="var(--red)" stroke-width="1.2"/><path d="M3 5.2 L4.5 6.5 L7 3.8" fill="none" stroke="var(--red)" stroke-width="1.2"/></svg>Balcony Systems</li>
      <li><svg viewBox="0 0 10 10"><circle cx="5" cy="5" r="4.2" fill="none" stroke="var(--red)" stroke-width="1.2"/><path d="M3 5.2 L4.5 6.5 L7 3.8" fill="none" stroke="var(--red)" stroke-width="1.2"/></svg>Sunshade Systems</li>
      <li><svg viewBox="0 0 10 10"><circle cx="5" cy="5" r="4.2" fill="none" stroke="var(--red)" stroke-width="1.2"/><path d="M3 5.2 L4.5 6.5 L7 3.8" fill="none" stroke="var(--red)" stroke-width="1.2"/></svg>Canopy Systems</li>
      <li><svg viewBox="0 0 10 10"><circle cx="5" cy="5" r="4.2" fill="none" stroke="var(--red)" stroke-width="1.2"/><path d="M3 5.2 L4.5 6.5 L7 3.8" fill="none" stroke="var(--red)" stroke-width="1.2"/></svg>Pation Cover Systems</li>
    </ul>

    <div class="abs contact contact-wa">
      <h3>WASHINGTON</h3>
      <p><svg viewBox="0 0 9 10"><path d="M4.5 10 C1 6 0.5 4.8 0.5 3.8 A4 4 0 0 1 8.5 3.8 C8.5 4.8 8 6 4.5 10 Z" fill="var(--red)"/><circle cx="4.5" cy="3.8" r="1.5" fill="#fff"/></svg>4127 Harlow Ridge Rd</p>
      <p class="indent">Alder Bend, WA 98911</p>
      <p><svg viewBox="0 0 9 10"><path d="M1.5 1 L3.2 0.8 L4 3 L3 3.8 Q4 6 5.8 7 L6.6 6 L8.6 6.8 L8.4 8.6 Q4 9 1 4 Z" fill="var(--red)"/></svg>253-555-0142</p>
      <p><svg viewBox="0 0 9 10"><rect x="1" y="3" width="7" height="6" rx="1" fill="var(--red)"/><rect x="2.5" y="1" width="4" height="2.5" fill="var(--red)"/></svg>877-555-0143</p>
    </div>

    <div class="abs contact contact-or">
      <h3>OREGON</h3>
      <p><svg viewBox="0 0 9 10"><path d="M4.5 10 C1 6 0.5 4.8 0.5 3.8 A4 4 0 0 1 8.5 3.8 C8.5 4.8 8 6 4.5 10 Z" fill="var(--red)"/><circle cx="4.5" cy="3.8" r="1.5" fill="#fff"/></svg>8620 NE Corliss Ave.</p>
      <p class="indent">Portland, OR 97299</p>
      <p><svg viewBox="0 0 9 10"><path d="M1.5 1 L3.2 0.8 L4 3 L3 3.8 Q4 6 5.8 7 L6.6 6 L8.6 6.8 L8.4 8.6 Q4 9 1 4 Z" fill="var(--red)"/></svg>503-555-0127</p>
      <p><svg viewBox="0 0 9 10"><rect x="1" y="3" width="7" height="6" rx="1" fill="var(--red)"/><rect x="2.5" y="1" width="4" height="2.5" fill="var(--red)"/></svg>503-555-0188</p>
    </div>

    <p class="abs headline">Stunning results applications to inspire</p>
    <div class="abs web">
      <svg viewBox="0 0 12 12" fill="none" stroke="#fff" stroke-width="1"><circle cx="6" cy="6" r="5"/><ellipse cx="6" cy="6" rx="2.2" ry="5"/><line x1="1" y1="6" x2="11" y2="6"/></svg>
      <span>velmorafabworks.example</span>
    </div>
  </div>
</div>
</body>
</html>
```